Business Card for a mobile physiotherapy company

I need a layout for a business card for a mobile physiotherapy company.
Slogan is "Mobile Physiotherapy - Your Road To Recovery"
Phone number is 867-412-5093
Email VantePhysio@mailbox-demo.ca (subject to change with website)
Website www.VantePhysio.ca
My name and credentials: Gil Varney Gil Varney, BSc(kin), MPT, CAFCI, IMS
Information maybe included: Direct Billing, Services including Physiotherapy, IMS, acupuncture
Maybe include facebook and instagram logos
One side with the logo clean and sharp
Other side with details, try not to look too busy, keep everything concise

```html
<!DOCTYPE html>
<html lang="en">
<head>
<meta charset="utf-8">
<title>Vante Physio – Business Card</title>
<link href="https://fonts.googleapis.com/css2?family=Roboto:wght@400;500;700&display=swap" rel="stylesheet">
<style>
  :root {
    --bg: #dcdcdc;
    --card: #ffffff;
    --blue: #3f5e8c;
    --green: #1b6b5d;
    --green-dark: #15594d;
    --ink: #2f2f2f;
  }
  * { box-sizing: border-box; margin: 0; padding: 0; }
  html, body {
    width: 1200px; height: 900px; overflow: hidden;
    background: var(--bg);
    font-family: 'Roboto', Arial, sans-serif;
  }
  .stage {
    width: 1200px; height: 900px;
    display: flex; flex-direction: column; align-items: center; justify-content: center;
    gap: 36px;
  }
  .card {
    position: relative;
    width: 700px; height: 400px;
    background: var(--card);
    box-shadow: 0 6px 18px rgba(0,0,0,0.15);
    overflow: hidden;
  }

  /* brand wordmark */
  .brand {
    display: flex; align-items: center; gap: 14px;
    color: var(--green);
    font-weight: 700;
    letter-spacing: 0.08em;
    text-transform: uppercase;
  }
  .brand-mark { background: var(--blue); flex: none; }

  /* logo side */
  .card-front .brand {
    position: absolute; left: 0; right: 0; top: 140px;
    justify-content: center;
    font-size: 46px;
  }
  .card-front .brand-mark { width: 30px; height: 30px; }
  .tagline {
    position: absolute; left: 0; right: 0; bottom: 58px;
    text-align: center;
    color: var(--green);
    font-size: 17px;
  }

  /* details side */
  .card-back .brand {
    position: absolute; left: 290px; top: 62px;
    font-size: 30px;
  }
  .card-back .brand-mark { width: 20px; height: 20px; }

  .person {
    position: absolute; left: 120px; top: 198px; width: 250px;
    text-align: right;
  }
  .person-name { color: var(--blue); font-size: 28px; font-weight: 700; }
  .person-credentials { color: var(--ink); font-size: 15px; margin-top: 6px; }

  .divider {
    position: absolute; left: 394px; top: 178px;
    width: 1.5px; height: 100px; background: var(--blue);
  }

  .contacts {
    position: absolute; left: 416px; top: 176px;
    list-style: none;
    display: flex; flex-direction: column; gap: 10px;
  }
  .contact { display: flex; align-items: center; gap: 10px; color: var(--ink); font-size: 15px; }
  .contact-icon {
    width: 24px; height: 24px; background: var(--blue);
    display: flex; align-items: center; justify-content: center; flex: none;
  }
  .contact-icon svg { width: 14px; height: 14px; }

  .services {
    position: absolute; left: 0; right: 0; bottom: 0; height: 70px;
    background: linear-gradient(90deg, var(--green), var(--green-dark));
    display: flex; align-items: center; justify-content: center; gap: 60px;
    list-style: none;
  }
  .service { display: flex; align-items: center; gap: 12px; color: #fff; font-size: 18px; }
  .service-box { width: 14px; height: 14px; background: #fff; flex: none; }
</style>
</head>
<body>
<main class="stage">

  <section class="card card-front" aria-label="Logo side">
    <div class="brand"><span class="brand-mark"></span>Vante Physio</div>
    <p class="tagline">Mobile Physiotherapy - Your Road To Recovery</p>
  </section>

  <section class="card card-back" aria-label="Details side">
    <div class="brand"><span class="brand-mark"></span>Vante Physio</div>

    <div class="person">
      <p class="person-name">Gil Varney</p>
      <p class="person-credentials">BSc(kin), MPT, CAFCI, IMS</p>
    </div>

    <span class="divider"></span>

    <ul class="contacts">
      <li class="contact">
        <span class="contact-icon">
          <svg viewBox="0 0 16 16" aria-hidden="true"><path fill="#fff" d="M3.5 1.5l2.5 0 1 3.5-1.6 1.2c.8 1.7 2.1 3 3.8 3.8l1.2-1.6 3.5 1v2.5c0 .8-.7 1.5-1.5 1.5C7 13.4 2.6 9 2 3c0-.8.7-1.5 1.5-1.5z"/></svg>
        </span>867-412-5093
      </li>
      <li class="contact">
        <span class="contact-icon">
          <svg viewBox="0 0 16 16" aria-hidden="true"><rect x="1.5" y="3.5" width="13" height="9" fill="none" stroke="#fff" stroke-width="1.4"/><path d="M1.5 3.5L8 9l6.5-5.5" fill="none" stroke="#fff" stroke-width="1.4"/></svg>
        </span>VantePhysio@mailbox-demo.ca
      </li>
      <li class="contact">
        <span class="contact-icon">
          <svg viewBox="0 0 16 16" aria-hidden="true"><g fill="none" stroke="#fff" stroke-width="1.2"><circle cx="8" cy="8" r="6.2"/><ellipse cx="8" cy="8" rx="2.8" ry="6.2"/><path d="M1.8 8h12.4M3 4.7h10M3 11.3h10"/></g></svg>
        </span>www.VantePhysio.ca
      </li>
    </ul>

    <ul class="services">
      <li class="service"><span class="service-box"></span>Physiotherapy</li>
      <li class="service"><span class="service-box"></span>IMS</li>
      <li class="service"><span class="service-box"></span>Acupuncture</li>
    </ul>
  </section>

</main>
</body>
</html>
```